Quimby's Yard & Garden Center Business Card Update

I need an updated Business card design for my Lawn and Garden Center. We do Landscaping installs, Lawn Mowing, Snow Removal and also have a Garden Center Retail Division. I uploaded a few of our previous business cards to give an idea of what we are starting with. The main goal of this update is to simplify and modernize the business card, not all of the services that are on the previous cards has to be on the new one but I would still like to highlight our main services. There is also a sample of our logo that Can be used in the design.

Industry/Entity Type

Landscaping

Contact Information for Business Card

Morris Quimby
Morris@Quimbysyardandgarden.example
Business (555) 201-7784
Cell (555) 318-6092

Colors

Designer to choose colors to be used in the design.

Requirements
Must have
• Services Provided :
• Landscaping
• Lawn Maintenance
• Snow Removal
• Garden Center

```html
<!DOCTYPE html>
<html lang="en">
<head>
<meta charset="utf-8">
<title>Quimby's Yard &amp; Garden Center – Business Card</title>
<link href="https://fonts.googleapis.com/css2?family=Open+Sans:wght@400;600;700&display=swap" rel="stylesheet">
<style>
  :root {
    --stage: #2e2f31;
    --card: #1d1e20;
    --card-edge: #26272a;
    --text: #f4f4f4;
    --muted: #d8d8d8;
    --rule: #55575b;
    --green: #2d5a27;
    --green-bright: #3f7a34;
    --pattern-a: #2a2b2e;
    --pattern-b: #222326;
  }
  * { box-sizing: border-box; margin: 0; padding: 0; }
  html, body { width: 1200px; height: 1108px; overflow: hidden; }
  body {
    background: var(--stage);
    font-family: "Open Sans", Arial, sans-serif;
    color: var(--text);
    position: relative;
  }
  .card {
    position: absolute;
    top: 174px;
    width: 440px;
    height: 760px;
    background: var(--card);
    border-radius: 26px;
    border: 1px solid var(--card-edge);
    overflow: hidden;
    text-align: center;
  }
  .card--front { left: 120px; }
  .card--back { left: 640px; }

  /* Front */
  .brand {
    margin-top: 130px;
    display: flex;
    flex-direction: column;
    align-items: center;
    gap: 6px;
  }
  .brand__row { display: flex; align-items: center; gap: 16px; }
  .brand__mark {
    width: 34px; height: 34px; border-radius: 50%;
    background: var(--green-bright);
  }
  .brand__name, .brand__sub {
    font-weight: 700;
    color: var(--text);
  }
  .brand__name { font-size: 56px; line-height: 1; }
  .brand__sub { font-size: 27px; margin-top: 6px; }

  .person {
    margin-top: 58px;
    font-size: 30px;
    font-weight: 700;
  }
  .icon-rule {
    margin: 18px auto 0;
    width: 340px;
    display: flex;
    align-items: center;
    gap: 12px;
  }
  .icon-rule::before, .icon-rule::after {
    content: ""; flex: 1; height: 1px; background: var(--rule);
  }
  .icon {
    width: 30px; height: 30px;
    background: var(--text);
    border-radius: 6px;
    display: flex; align-items: center; justify-content: center;
  }
  .icon svg { width: 18px; height: 18px; }
  .contact {
    margin-top: 14px;
    font-size: 21px;
    line-height: 1.35;
    color: var(--muted);
  }
  .contact__email { font-size: 19px; }
  .rule {
    width: 340px; height: 1px; background: var(--rule);
    margin: 22px auto 18px;
  }
  .company { font-size: 21px; font-weight: 700; }
  .address { font-size: 20px; color: var(--muted); margin-top: 2px; }

  /* Back */
  .pattern {
    position: absolute; left: 0; top: 0; width: 100%; height: 470px;
    background: linear-gradient(180deg, var(--pattern-a) 0%, var(--pattern-b) 100%);
  }
  .back__mark {
    position: absolute; left: 50%; top: 410px;
    width: 70px; height: 70px; margin-left: -35px;
    border-radius: 50%; background: var(--green-bright);
  }
  .back__content {
    position: absolute; left: 0; right: 0; top: 520px;
  }
  .website { font-size: 21px; color: var(--muted); }
  .back__rule {
    width: 160px; height: 2px; background: var(--green);
    margin: 22px auto 24px;
  }
  .services { list-style: none; font-size: 22px; line-height: 1.35; color: var(--muted); }
  .services .dot {
    display: inline-block; width: 11px; height: 11px; border-radius: 50%;
    background: var(--green-bright); margin: 0 6px; vertical-align: middle;
  }
</style>
</head>
<body>
  <section class="card card--front">
    <div class="brand">
      <div class="brand__row">
        <span class="brand__mark"></span>
        <span class="brand__name">Quimby's</span>
      </div>
      <span class="brand__sub">Yard &amp; Garden Center</span>
    </div>

    <p class="person">Morris Quimby</p>

    <div class="icon-rule">
      <span class="icon" aria-label="Phone">
        <svg viewBox="0 0 24 24"><path fill="#2d5a27" d="M6.6 10.8a15 15 0 0 0 6.6 6.6l2.2-2.2c.3-.3.7-.4 1-.2 1.1.4 2.3.6 3.6.6.6 0 1 .4 1 1V20c0 .6-.4 1-1 1A17 17 0 0 1 3 4c0-.6.4-1 1-1h3.5c.6 0 1 .4 1 1 0 1.3.2 2.5.6 3.6.1.3 0 .7-.2 1z"/></svg>
      </span>
      <span class="icon" aria-label="Mobile">
        <svg viewBox="0 0 24 24"><rect x="6" y="2" width="12" height="20" rx="2" fill="none" stroke="#2d5a27" stroke-width="2.2"/><circle cx="12" cy="18" r="1.3" fill="#2d5a27"/></svg>
      </span>
      <span class="icon" aria-label="Email">
        <svg viewBox="0 0 24 24"><rect x="2" y="5" width="20" height="14" rx="1.5" fill="#2d5a27"/><path d="M3 6l9 7 9-7" fill="none" stroke="#f4f4f4" stroke-width="1.6"/></svg>
      </span>
    </div>

    <div class="contact">
      <p>(555) 201-7784</p>
      <p>(555) 318-6092</p>
      <p class="contact__email">Morris@Quimbysyardandgarden.example</p>
    </div>

    <div class="rule"></div>

    <p class="company">Quimby's Yard &amp; Garden Center</p>
    <p class="address">48 Meadow Row, Fairview, ST 00000</p>
  </section>

  <section class="card card--back">
    <div class="pattern" role="img" aria-label="Faint repeating tree emblem pattern"></div>
    <span class="back__mark"></span>
    <div class="back__content">
      <p class="website">www.quimbysyardandgarden.example</p>
      <div class="back__rule"></div>
      <ul class="services">
        <li>Landscape Design &amp; Installation</li>
        <li>Lawn Maintenance</li>
        <li>Snow Removal<span class="dot"></span>Garden Center</li>
      </ul>
    </div>
  </section>
</body>
</html>
```